Your Harbor Weekend book cover design

I have attached an image that I would like this front cover to be similar to. This is a book about marriage so there will need to be a man and woman on the front cover and I am open to your creative design from that point. I have also attached the ISBN barcode and photo of authors for back cover. Book details are below:

Title:
Your HARBOR WEEKEND
Tending Wedlock
A Handbook for Your Home and Household

Authors: LEN AND MAVE’ HOLBURN
Book size : 8x10
Back cover text:
LEN AND MAVE’ HOLBURN

Authors, parents, grandparents, business owners, and public speakers, has served in ministry for over 25 years. They are the founders of Stand Firm Global Fellowship, serving as the senior pastors. They are also currently serving as national and international mission directors. They both are very intentional about assisting couples in developing their marriages. Having firsthand knowledge of God’s mercy in this area, the Holburns are sharing the power of Tending Wedlock with dedication and simplicity.

They are blessed to have three married children, and thirteen grandchildren in their more than 40 years of marriage. They are currently residing in Birmingham, Alabama. They look forward seeing you soon.

Back cover photo: Attached

```html
<!DOCTYPE html>
<html lang="en">
<head>
<meta charset="UTF-8">
<title>Your Harbor Weekend — Book Cover</title>
<link rel="stylesheet" href="https://fonts.googleapis.com/css2?family=Cinzel:wght@400;700&family=EB+Garamond:ital,wght@0,700;1,700&family=Lato:wght@400&display=swap">
<style>
  :root {
    --cover-bg: #fad4cb;
    --ink: #1f1f1f;
    --title-ink: #2b2b2b;
    --accent-coral: #ef7b5f;
    --art-peach: #f9c29a;
    --art-warm: #f4a27a;
    --art-coral: #ec7c5c;
    --art-leaf: #9fcdc2;
  }
  * { margin: 0; padding: 0; box-sizing: border-box; }
  html, body { width: 960px; height: 1200px; overflow: hidden; }
  body { background: var(--cover-bg); }
  .cover {
    position: relative;
    width: 960px;
    height: 1200px;
    background: var(--cover-bg);
    color: var(--ink);
  }
  .eyebrow {
    position: absolute;
    top: 112px; left: 0; width: 100%;
    text-align: center;
    font-family: "Lato", sans-serif;
    font-size: 24px;
    letter-spacing: 0.12em;
    color: var(--accent-coral);
  }
  .title-line {
    position: absolute;
    left: 0; width: 100%;
    text-align: center;
    font-family: "Cinzel", serif;
    font-weight: 400;
    color: var(--title-ink);
    line-height: 1;
    text-shadow: 0 1px 1px rgba(0,0,0,0.25);
  }
  .title-line--first {
    top: 156px;
    font-size: 108px;
    letter-spacing: 0.14em;
    padding-left: 0.14em;
  }
  .title-line--second {
    top: 278px;
    font-size: 108px;
    letter-spacing: 0.1em;
    padding-left: 0.1em;
  }
  .subtitle {
    position: absolute;
    top: 404px; left: 0; width: 100%;
    text-align: center;
    font-family: "Lato", sans-serif;
    font-size: 27px;
    letter-spacing: 0.1em;
    color: var(--ink);
  }
  .cover-art {
    position: absolute;
    left: 164px; top: 476px;
    width: 640px; height: 516px;
  }
  .tagline {
    position: absolute;
    top: 1036px; left: 0; width: 100%;
    text-align: center;
    font-family: "EB Garamond", serif;
    font-style: italic;
    font-weight: 700;
    font-size: 26px;
    color: var(--ink);
  }
  .authors {
    position: absolute;
    top: 1090px; left: 0; width: 100%;
    text-align: center;
    font-family: "EB Garamond", serif;
    font-weight: 700;
    font-size: 41px;
    letter-spacing: 0.08em;
    color: #111;
  }
</style>
</head>
<body>
  <main class="cover">
    <p class="eyebrow">YOUR</p>
    <h1>
      <span class="title-line title-line--first">HARBOR</span>
      <span class="title-line title-line--second">WEEKEND</span>
    </h1>
    <p class="subtitle">TENDING WEDLOCK</p>

    <svg class="cover-art" viewBox="0 0 640 516" role="img" aria-label="Illustration of an embracing couple with red hair, surrounded by a round wreath of leaves, flowers, small hearts and two birdhouses">
      <defs>
        <radialGradient id="artTones" cx="50%" cy="48%" r="50%">
          <stop offset="0%" stop-color="var(--art-peach)"/>
          <stop offset="45%" stop-color="var(--art-warm)"/>
          <stop offset="75%" stop-color="var(--art-coral)"/>
          <stop offset="100%" stop-color="var(--art-leaf)"/>
        </radialGradient>
      </defs>
      <circle cx="320" cy="258" r="256" fill="url(#artTones)"/>
    </svg>

    <p class="tagline">A Handbook for Your Home and Household</p>
    <p class="authors">LEN AND MAVE’ HOLBURN</p>
  </main>
</body>
</html>
```